Clean and modern business cards

Looking for an updated business card design for my dental office “corvanta dental” . Looking for a modern clean / sleek design . I’m thinking black background but open to seeing other options . One side needs to have an appointment card . Card needs to have logo, dentist name , phone, email , address . I’ve attached couple of cards I thought were cool as well as my logo
Target Market(s)
Dental patients
Industry/Entity Type
Dentistry
Contact Information for Business Card
Phone email address

```html
<!DOCTYPE html>
<html lang="en">
<head>
<meta charset="utf-8">
<title>Corvanta Dental – Business &amp; Appointment Card</title>
<link rel="stylesheet" href="https://fonts.googleapis.com/css2?family=Montserrat:wght@300;400;600;700&display=swap">
<style>
  :root {
    --page-bg: #ededed;
    --card-black: #000000;
    --card-white: #ffffff;
    --ink: #2b2b2b;
    --ink-soft: #555555;
    --line: #8a8a8a;
    --watermark: #e6e6e6;
    --accent-teal: #1aa3b8;
    --accent-purple: #7b2a8f;
    --accent-yellow: #f2c01e;
    --accent-green: #8cbc2a;
    --accent-orange: #f04e1e;
    --accent-blue: #1d4f9c;
  }
  * { box-sizing: border-box; margin: 0; padding: 0; }
  html, body {
    width: 1200px; height: 1200px; overflow: hidden;
    background: var(--page-bg);
    font-family: "Montserrat", sans-serif;
  }
  .canvas { position: relative; width: 1200px; height: 1200px; }

  /* Front */
  .card-front {
    position: absolute; left: 270px; top: 260px;
    width: 526px; height: 300px;
    background: var(--card-black);
  }
  .card-front .brand-dot {
    position: absolute; left: 223px; top: 70px;
    width: 80px; height: 80px; border-radius: 50%;
    background: var(--card-white);
  }
  .card-front .brand-name {
    position: absolute; left: 0; right: 0; top: 178px;
    text-align: center; color: var(--card-white);
    font-weight: 700; font-size: 19px; letter-spacing: 0.42em;
    padding-left: 0.42em;
  }

  /* Back */
  .card-back {
    position: absolute; left: 388px; top: 602px;
    width: 525px; height: 299px;
    background: var(--card-white);
    overflow: hidden;
  }
  .confetti-strip {
    position: absolute; left: 0; top: 64px;
    width: 38px; height: 174px;
    background: linear-gradient(180deg, var(--accent-yellow), var(--accent-teal) 30%, var(--accent-purple) 55%, var(--accent-green) 75%, var(--accent-teal));
    border-radius: 0 19px 19px 0;
  }
  .side-name {
    position: absolute; right: 0; top: 0; height: 299px;
    display: flex; flex-direction: row-reverse; align-items: center;
    color: var(--watermark); line-height: 1;
  }
  .side-name span { writing-mode: vertical-rl; transform: rotate(180deg); }
  .side-name .side-name-large { font-weight: 700; font-size: 58px; letter-spacing: 0.06em; margin-right: -6px; }
  .side-name .side-name-small { font-weight: 700; font-size: 24px; letter-spacing: 0.22em; margin-right: 4px; }

  .appointment {
    position: absolute; left: 0; width: 516px; top: 84px;
    text-align: center; color: var(--ink);
  }
  .appointment-title { font-weight: 400; font-size: 13px; }
  .appointment-field {
    position: relative; width: 128px; height: 19px;
    margin: 9px auto 0; border: 1px solid var(--line);
  }
  .appointment-field + .appointment-field { margin-top: 12px; }
  .appointment-field span {
    position: absolute; left: 50%; top: -9px; transform: translateX(-50%);
    background: var(--card-white); padding: 0 3px;
    font-size: 12.5px; font-weight: 400; line-height: 16px;
  }
  .appointment-note {
    margin-top: 16px; font-size: 10.5px; font-weight: 400; line-height: 1.3;
  }
  .contact {
    position: absolute; left: 0; width: 516px; top: 263px;
    text-align: center; color: var(--ink-soft);
    font-size: 8px; font-weight: 400; line-height: 1.5;
  }
</style>
</head>
<body>
<main class="canvas">
  <section class="card-front" aria-label="Card front">
    <div class="brand-dot"></div>
    <h1 class="brand-name">CORVANTA DENTAL</h1>
  </section>

  <section class="card-back" aria-label="Appointment card back">
    <div class="confetti-strip" role="img" aria-label="Multicoloured confetti dots along the left edge"></div>
    <div class="side-name" aria-hidden="true">
      <span class="side-name-large">DENTAL</span>
      <span class="side-name-small">CORVANTA</span>
    </div>
    <div class="appointment">
      <p class="appointment-title">Your Next Appointment is:</p>
      <div class="appointment-field"><span>Date</span></div>
      <div class="appointment-field"><span>Time</span></div>
      <p class="appointment-note">To cancel or reschedule please notify us at least<br>48 hours prior to your scheduled appointment</p>
    </div>
    <address class="contact">
      2480 LARKFIELD AVE, WINNIPEG, MB<br>
      (204) 555-0172 &nbsp;•&nbsp; CORVANTAWPG.CA &nbsp;•&nbsp; CONTACT@CORVANTAWPG.CA
    </address>
  </section>
</main>
</body>
</html>
```